Fernvale Craft Works business card design- Fine Art sculpture business (Contract guaranteed)

This business card is for a fine art business. Though we don't have a website up and running yet it should be up soon. I would like the business card to be elegant and fairly simple with a picture of one of my sculptures on the front (you might need to photoshop out the background) as well as my basic contact info (my name,phone # and e-mail). On the back I'd like it to be pretty simple with just "Notes" and some blank lines for writing in info.

Target Market(s)

High end artwork buyers

Industry/Entity Type

Art Gallery

Contact Information for Business Card

Marlo Prewitt Phone: (555) 213-4098 E-mail: marlo@quillbrookmail.com Facebook: @fernvalecraftworks Instagram: fernvalecraftworks

Colors

Designer to choose colors to be used in the design.

Requirements
Must have
• *A picture of one of my sculptures*, my name, business name (Fernvale Craft Works), e-mail, phone #, and a notes section on the back.
• Fernvale Craft Works
• Marlo Prewitt
• (555)213-4098
• marlo@quillbrookmail.com
• Facebook: @fernvalecraftworks
• Instagram: fernvalecraftworks
Nice to have
• It'd be nice if you can crop out the background in the sculpture pictures, which ever one you end up using.

```html
<!DOCTYPE html>
<html lang="en">
<head>
<meta charset="utf-8">
<title>Fernvale Craft Works – Business Card</title>
<link rel="stylesheet" href="https://fonts.googleapis.com/css2?family=Jost:wght@400&family=Lato:wght@400&display=swap">
<style>
  :root {
    --page-bg: #ebe8e3;
    --card-bg: #ffffff;
    --lavender: #e4def0;
    --accent: #7b3fa0;
    --frame: #5a5a5a;
    --ink: #2f2f33;
    --crystal-light: #8f5fd0;
    --crystal-mid: #4d2a8c;
    --crystal-dark: #1e1640;
  }
  html, body {
    margin: 0;
    width: 1200px;
    height: 1200px;
    overflow: hidden;
    background: var(--page-bg);
  }
  .sheet {
    position: relative;
    width: 1200px;
    height: 1200px;
  }
  .card {
    position: absolute;
    left: 110px;
    width: 980px;
    height: 560px;
    background: var(--card-bg);
    box-shadow: 0 6px 20px rgba(0,0,0,0.15);
    overflow: hidden;
  }
  .card--front { top: 25px; }
  .card--back { top: 615px; }
  .card svg { display: block; }
  .name { font-family: "Jost", sans-serif; font-size: 42px; fill: var(--ink); }
  .contact { font-family: "Lato", sans-serif; font-size: 25px; fill: var(--ink); letter-spacing: 0.5px; }
  .notes-title { font-family: "Jost", sans-serif; font-size: 42px; fill: var(--ink); }
  .icon { fill: none; stroke: var(--accent); stroke-width: 2; stroke-linecap: round; stroke-linejoin: round; }
</style>
</head>
<body>
<main class="sheet">

  <section class="card card--front" aria-label="Business card front">
    <svg width="980" height="560" viewBox="0 0 980 560">
      <defs>
        <linearGradient id="crystalTone" x1="0" y1="0" x2="1" y2="1">
          <stop offset="0" stop-color="var(--crystal-light)"/>
          <stop offset="0.55" stop-color="var(--crystal-mid)"/>
          <stop offset="1" stop-color="var(--crystal-dark)"/>
        </linearGradient>
        <clipPath id="frontCircle"><circle cx="-90" cy="390" r="510"/></clipPath>
      </defs>
      <circle class="accent-circle" cx="-90" cy="390" r="510" fill="var(--lavender)"/>

      <g class="frame">
        <rect x="58" y="48" width="868" height="466" fill="none" stroke="var(--frame)" stroke-width="1.5"/>
        <rect x="58" y="48" width="868" height="466" fill="none" stroke="var(--accent)" stroke-width="1.5" clip-path="url(#frontCircle)"/>
        <rect x="905" y="36" width="16" height="16" fill="none" stroke="var(--frame)" stroke-width="1.5"/>
        <rect x="905" y="504" width="16" height="16" fill="none" stroke="var(--frame)" stroke-width="1.5"/>
        <rect x="64" y="504" width="16" height="16" fill="none" stroke="var(--accent)" stroke-width="1.5"/>
      </g>

      <path class="sculpture-photo" role="img" aria-label="Photograph of an amethyst crystal geode sculpture"
            d="M0 30 L70 20 L180 18 L260 40 L330 70 L390 110 L430 170 L460 240 L450 300 L420 360 L410 420 L380 480 L340 530 L300 560 L210 560 L180 500 L150 440 L100 380 L40 330 L0 300 Z"
            fill="url(#crystalTone)"/>

      <text class="name" x="555" y="155">Marlo Prewitt</text>

      <g class="contact-list">
        <path class="icon" d="M562 310 c-4 0 -6 4 -4 8 c4 8 10 14 18 17 c4 1 7 -1 7 -4 l-5 -4 l-4 3 c-4 -2 -7 -5 -9 -9 l3 -4 z"/>
        <text class="contact" x="600" y="330">(555) 213-4098</text>

        <circle class="icon" cx="572" cy="382" r="10"/>
        <circle class="icon" cx="572" cy="382" r="4"/>
        <text class="contact" x="600" y="390">marlo@quillbrookmail.com</text>

        <circle cx="572" cy="442" r="7" fill="var(--accent)"/>
        <text class="contact" x="600" y="450">@fernvalecraftworks</text>
      </g>
    </svg>
  </section>

  <section class="card card--back" aria-label="Business card back">
    <svg width="980" height="560" viewBox="0 0 980 560">
      <defs>
        <clipPath id="backCircle"><circle cx="-70" cy="190" r="530"/></clipPath>
      </defs>
      <circle class="accent-circle" cx="-70" cy="190" r="530" fill="var(--lavender)"/>

      <g class="frame">
        <path d="M390 50 L58 50 L58 512 L922 512 L922 50 L545 50" fill="none" stroke="var(--frame)" stroke-width="1.5"/>
        <path d="M390 50 L58 50 L58 512 L922 512" fill="none" stroke="var(--accent)" stroke-width="1.5" clip-path="url(#backCircle)"/>
        <rect x="900" y="40" width="16" height="16" fill="none" stroke="var(--frame)" stroke-width="1.5"/>
        <rect x="900" y="500" width="16" height="16" fill="none" stroke="var(--frame)" stroke-width="1.5"/>
        <rect x="64" y="40" width="16" height="16" fill="none" stroke="var(--accent)" stroke-width="1.5"/>
      </g>

      <text class="notes-title" x="467" y="64" text-anchor="middle">Notes</text>

      <g class="writing-lines" stroke="var(--frame)" stroke-width="1.5">
        <line x1="100" y1="125" x2="880" y2="125"/>
        <line x1="100" y1="180" x2="880" y2="180"/>
        <line x1="100" y1="235" x2="880" y2="235"/>
        <line x1="100" y1="290" x2="880" y2="290"/>
        <line x1="100" y1="345" x2="880" y2="345"/>
        <line x1="100" y1="400" x2="880" y2="400"/>
        <line x1="100" y1="455" x2="880" y2="455"/>
      </g>
      <g class="writing-lines" stroke="var(--accent)" stroke-width="1.5" clip-path="url(#backCircle)">
        <line x1="100" y1="125" x2="880" y2="125"/>
        <line x1="100" y1="180" x2="880" y2="180"/>
        <line x1="100" y1="235" x2="880" y2="235"/>
        <line x1="100" y1="290" x2="880" y2="290"/>
        <line x1="100" y1="345" x2="880" y2="345"/>
        <line x1="100" y1="400" x2="880" y2="400"/>
        <line x1="100" y1="455" x2="880" y2="455"/>
      </g>
    </svg>
  </section>

</main>
</body>
</html>
```